Quorvan Medical business cards

Double sided business cards.

Medical technology consulting company.

Business cards with two names on the front, upper to middle left:

Dr Colin R. Harbury BMed GAICD +61412558907
Dr Owen Palatsky PhD MCommrclLaw +61437619042

Email and website addresses bottom right:

colin@quorvanmedical.com.au
www.quorvanmedical.com.au

Tree logo (as per attached file) on front in a suitable position.

Tag line (as per attached files) on the back.

Need a file format to upload to Paper Haven or Cardlyner.

```html
<!DOCTYPE html>
<html lang="en">
<head>
<meta charset="utf-8">
<title>Quorvan Medical business cards</title>
<link rel="stylesheet" href="https://fonts.googleapis.com/css2?family=Montserrat:wght@400;500;600;700&display=swap">
<style>
  :root {
    --bg: #4a4a4c;
    --bg-light: #6a6a6c;
    --green: #3fae3a;
    --green-card: #44b03c;
    --green-pattern: #3a9f34;
    --brown: #3b1a16;
    --rule: #8a6a66;
    --white: #ffffff;
    --text-grey: #555555;
  }
  * { margin: 0; padding: 0; box-sizing: border-box; }
  html, body { width: 1200px; height: 900px; overflow: hidden; }
  body {
    background: radial-gradient(ellipse at 60% 40%, var(--bg-light), var(--bg) 75%);
    font-family: "Montserrat", sans-serif;
    position: relative;
  }
  .card {
    position: absolute;
    width: 600px;
    height: 343px;
    border-radius: 22px;
    overflow: hidden;
    box-shadow: 0 10px 24px rgba(0,0,0,0.35);
  }
  /* Back side */
  .card-back {
    left: 70px;
    top: 60px;
    background: var(--green-card);
  }
  .back-pattern {
    position: absolute;
    inset: 0;
    background: radial-gradient(ellipse at 30% 60%, #5fbf3a, var(--green-pattern) 80%);
  }
  .back-brand {
    position: absolute;
    left: 380px;
    top: 150px;
    color: var(--white);
    font-weight: 600;
    font-size: 18px;
    letter-spacing: 1px;
    text-transform: uppercase;
  }
  /* Front side */
  .card-front {
    left: 530px;
    top: 490px;
    background: var(--white);
    color: var(--brown);
  }
  .brand {
    position: absolute;
    left: 0;
    right: 0;
    top: 58px;
    text-align: center;
  }
  .brand-name {
    font-size: 34px;
    font-weight: 400;
    letter-spacing: 0.5px;
    text-transform: uppercase;
    color: var(--green);
  }
  .tagline {
    margin-top: 6px;
    font-size: 13px;
    color: var(--green);
  }
  .tagline .sep { color: var(--brown); margin: 0 4px; }
  .rule {
    position: absolute;
    left: 40px;
    right: 40px;
    height: 1px;
    background: var(--rule);
  }
  .rule-top { top: 158px; }
  .rule-bottom { top: 268px; }
  .people {
    position: absolute;
    left: 40px;
    top: 178px;
  }
  .person {
    white-space: nowrap;
    line-height: 38px;
    font-size: 12.5px;
  }
  .person .name {
    font-size: 22px;
    font-weight: 700;
    color: var(--green);
    margin-right: 6px;
  }
  .person .quals { color: var(--brown); }
  .person .phone-label { color: var(--green); margin-left: 4px; }
  .contacts {
    position: absolute;
    left: 40px;
    right: 40px;
    top: 282px;
    display: flex;
    justify-content: space-between;
    font-size: 15px;
    color: var(--text-grey);
  }
  .contact { display: flex; align-items: center; gap: 8px; }
  .contact svg { width: 16px; height: 16px; }
</style>
</head>
<body>

  <section class="card card-back" aria-label="Card back">
    <div class="back-pattern" role="img" aria-label="Repeating embossed tree pattern across green background"></div>
    <div class="back-brand">Quorvan Medical</div>
  </section>

  <section class="card card-front" aria-label="Card front">
    <div class="brand">
      <div class="brand-name">Quorvan Medical</div>
      <div class="tagline">Concept<span class="sep">|</span>Commercialisation<span class="sep">|</span>Beyond</div>
    </div>

    <div class="rule rule-top"></div>

    <div class="people">
      <div class="person">
        <span class="name">Dr Owen Palatsky</span>
        <span class="quals">(PhD MCommrclLaw)</span>
        <span class="phone-label">P :</span> <span class="quals">+61437619042</span>
      </div>
      <div class="person">
        <span class="name">Dr Colin R. Harbury</span>
        <span class="quals">(BMed GAICD)</span>
        <span class="phone-label">P :</span> <span class="quals">+61412558907</span>
      </div>
    </div>

    <div class="rule rule-bottom"></div>

    <div class="contacts">
      <div class="contact">
        <svg viewBox="0 0 16 16" aria-hidden="true">
          <rect x="1" y="3" width="14" height="10" rx="1.5" fill="var(--green)"/>
          <path d="M1.5 4 L8 9 L14.5 4" fill="none" stroke="#fff" stroke-width="1.4"/>
        </svg>
        <span>colin@quorvanmedical.com.au</span>
      </div>
      <div class="contact">
        <svg viewBox="0 0 16 16" aria-hidden="true">
          <circle cx="8" cy="8" r="6.5" fill="none" stroke="var(--green)" stroke-width="1.6"/>
          <ellipse cx="8" cy="8" rx="2.8" ry="6.5" fill="none" stroke="var(--green)" stroke-width="1.2"/>
          <line x1="1.5" y1="8" x2="14.5" y2="8" stroke="var(--green)" stroke-width="1.2"/>
        </svg>
        <span>www.quorvanmedical.com.au</span>
      </div>
    </div>
  </section>

</body>
</html>
```